Website design for a high-end equestrian business

Design a website to replace current one. Clean, simple, elegant design. I run a business training show jumping riders and horses, as well as buying and selling high quality horses. I run my business from a beautiful yard in Co. Kildare, Ireland. Reference to Ireland and quality sport horses is important in the website.

Current website is www.helenacarrowmere.com. One page in particular that I need is a "Sport Horses" page as well as a "References" page. Layout for each to be similar to this one - https://www.brayleymeadow.net/en/sporthorses

Another website I like the feel of is www.veltrahunters.com
Colour theme to be charcoal grey with elements of lighter grey and cream, as per logo. Charcoal grey to be somewhat transparent, otherwise it takes over too much. Cream colour is also to be subtle and not too beige.

Please note that Carrowmere is one word.

Please note there are new photographs with which to work if desired.
Updates

Sick

Target Market(s)

Upmarket clients seeking high quality coaching services and high quality show jumping horses

Number of Pages Required

2 page

Font styles to use
Serif
Sans Serif

Colors

Designer to choose only greyscale colors for use in the design.

Requirements
Must have
• A clean, simple, elegant look to the final design. OVerall theme colours must be subtle and include charcoal grey, light grey and cream. A design that will work well for mobile also. Please include only photographs provided or on the old website.
Nice to have
• artistically integrated photographs. use of the logo.
Should not have
• Anything fussy.

```html
<!DOCTYPE html>
<html lang="en">
<head>
<meta charset="utf-8">
<title>Horses | Helena Carrowmere</title>
<link rel="stylesheet" href="https://fonts.googleapis.com/css2?family=Montserrat:wght@300;400;600;700&family=Cormorant+Garamond:ital,wght@0,500;1,500&display=swap">
<style>
:root{
  --gold:#c8b27a;
  --gold-dark:#b59d62;
  --cream:#f3efe2;
  --ink:#2b2b2b;
  --charcoal:#252525;
  --white:#ffffff;
  --light:#f6f6f4;
}
*{margin:0;padding:0;box-sizing:border-box}
html,body{width:755px;height:1200px;overflow:hidden;background:var(--white)}
body{position:relative;font-family:'Montserrat',sans-serif;color:var(--ink)}
.abs{position:absolute}

.topline{left:0;top:0;width:755px;height:3px;background:var(--gold)}
.header{left:0;top:3px;width:755px;height:60px;background:var(--white)}
.brand{left:104px;top:16px;font-family:'Cormorant Garamond',serif;font-size:26px;font-weight:500;color:var(--ink);display:flex;align-items:center;gap:6px}
.brand-dot{width:14px;height:14px;border-radius:50%;background:var(--gold)}
.nav{left:207px;top:27px;display:flex;font-size:7px;gap:0}
.nav span{position:absolute;white-space:nowrap}
.nav .active{color:var(--gold);font-weight:600}
.icons{left:590px;top:26px}

.hero{left:0;top:63px;width:755px;height:290px}
.hero-photo{position:absolute;inset:0;background:linear-gradient(180deg,#5a6a8a 0%,#6b5a4e 45%,#3d4f7a 75%,#d9c24a 100%)}
.hero-title{left:108px;top:172px;font-size:44px;font-weight:300;color:var(--white);letter-spacing:.5px}
.scroll-btn{left:259px;top:333px;width:32px;height:32px;border-radius:50%;background:var(--white);box-shadow:0 1px 4px rgba(0,0,0,.15)}

.horses{left:0;top:310px;width:755px;height:508px;background:linear-gradient(180deg,#f1ecdd,#f4f0e4 60%,#efe8d6)}
.card{position:absolute;width:182px}
.card-photo{width:182px;height:137px;background:linear-gradient(180deg,#9fb0c4 0%,#8a6a4c 55%,#6f8a4a 100%)}
.card-label{position:absolute;left:7px;top:117px;width:167px;height:36px;background:var(--gold);border-radius:3px;color:var(--white);text-align:center}
.card-label h3{font-size:10.5px;font-weight:300;margin-top:7px}
.card-label p{font-size:6.3px;font-weight:300;margin-top:1px}

.sponsors{left:0;top:818px;width:755px;height:120px;background:var(--light)}
.pill{position:absolute;top:28px;height:48px;border:1px solid #dcdcdc;border-radius:24px;background:var(--white);display:flex;align-items:center;justify-content:center;font-size:10px;font-weight:600;color:var(--ink)}

.footer-bg{left:0;top:900px;width:755px;height:262px}
.f-brand{left:121px;top:975px;font-family:'Cormorant Garamond',serif;font-size:34px;font-weight:500;color:var(--white);display:flex;align-items:center;gap:8px}
.f-brand .brand-dot{width:18px;height:18px}
.f-text{color:var(--white);font-size:7.6px;font-weight:400}
.links-title{left:283px;top:962px;font-size:12.5px;font-weight:700;color:var(--white)}
.links a{position:absolute;left:292px;color:var(--white);font-size:7px;text-decoration:none}
.map{left:398px;top:972px;width:257px;height:178px;border-radius:26px;background:linear-gradient(135deg,#efefed,#e6e6e3)}
.social{top:1131px;width:11px;height:11px;background:#3b6fb5}
.copyright{left:0;top:1174px;width:755px;height:26px;background:var(--gold);color:var(--white);font-size:7.5px;text-align:center;line-height:26px}
</style>
</head>
<body>
<div class="abs topline"></div>
<header class="abs header"></header>
<div class="abs brand"><span>HC</span><span class="brand-dot"></span></div>
<nav class="abs nav">
  <span style="left:0">Home</span>
  <span style="left:45px">About</span>
  <span class="active" style="left:90px">Horses ⌄</span>
  <span style="left:139px">Sponsors</span>
  <span style="left:194px">Facilities &amp; Services ⌄</span>
  <span style="left:282px">Gallery</span>
  <span style="left:330px">Contact Us</span>
</nav>
<svg class="abs icons" width="50" height="16" viewBox="0 0 50 16">
  <circle cx="7" cy="6" r="4" fill="none" stroke="#333" stroke-width="1.2"/>
  <line x1="4" y1="9" x2="1" y2="13" stroke="#333" stroke-width="1.5"/>
  <rect x="22" y="4" width="10" height="1.6" fill="#333"/><rect x="22" y="7.3" width="10" height="1.6" fill="#333"/><rect x="22" y="10.6" width="10" height="1.6" fill="#333"/>
  <rect x="43" y="5" width="6" height="8" fill="none" stroke="#555" stroke-width="1"/>
  <path d="M44.5 5 v-2 a1.5 1.5 0 0 1 3 0 v2" fill="none" stroke="#555"/>
</svg>

<section class="abs horses"></section>

<div class="abs hero">
  <div class="hero-photo" role="img" aria-label="Rider on a bay horse clearing a show jump in front of a packed grandstand"></div>
</div>
<svg class="abs" style="left:0;top:300px" width="755" height="60" viewBox="0 0 755 60">
  <path d="M0 10 L272 45 L755 8 L755 60 L0 60 Z" fill="#f2eddf"/>
  <path d="M0 10 L272 45 L755 8" fill="none" stroke="var(--gold)" stroke-width="2"/>
</svg>
<h1 class="abs hero-title">Horses</h1>
<div class="abs scroll-btn">
  <svg width="32" height="32" viewBox="0 0 32 32"><path d="M10 11 l6 5 l6-5 M10 16 l6 5 l6-5" fill="none" stroke="var(--gold)" stroke-width="1.8"/></svg>
</div>

<div class="card" style="left:89px;top:419px"><div class="card-photo" role="img" aria-label="Bay gelding jumping at an arena"></div><div class="card-label"><h3>Corrib Star 2013 gelding</h3><p>Arandor X Fairlight</p></div></div>
<div class="card" style="left:287px;top:419px"><div class="card-photo" role="img" aria-label="Bay stallion clearing a striped fence"></div><div class="card-label"><h3>HC Eamon 2009 stallion</h3><p>Castor van Mere X Lindow</p></div></div>
<div class="card" style="left:484px;top:419px"><div class="card-photo" role="img" aria-label="Chestnut gelding jumping on a sand arena"></div><div class="card-label"><h3>HC Ronan 2010 gelding</h3><p>Lowan X Le Clos de Sarn</p></div></div>
<div class="card" style="left:89px;top:602px"><div class="card-photo" role="img" aria-label="Rider on a bay horse in the ring"></div><div class="card-label"><h3>HC Kilbride 2010 gelding</h3><p>Lucetto X Crossfield</p></div></div>
<div class="card" style="left:287px;top:602px"><div class="card-photo" role="img" aria-label="Chestnut mare jumping an oxer"></div><div class="card-label"><h3>Quillmara 2009 mare</h3><p>Quintus de Rove X Carmello</p></div></div>
<div class="card" style="left:484px;top:602px"><div class="card-photo" role="img" aria-label="Grey gelding jumping under a cloudy sky"></div><div class="card-label"><h3>Prestance 1997 gelding</h3><p>Andoro X Emeril</p></div></div>

<section class="abs sponsors">
  <div class="pill" style="left:97px;width:110px">Brookwell</div>
  <div class="pill" style="left:216px;width:88px">Seaforage Equine</div>
  <div class="pill" style="left:313px;width:110px">Lanmore Rugs</div>
  <div class="pill" style="left:435px;width:82px">Stirrup Line</div>
  <div class="pill" style="left:523px;width:82px">Velocra</div>
  <div class="pill" style="left:614px;width:58px">Aria</div>
</section>

<svg class="abs footer-bg" width="755" height="274" viewBox="0 0 755 274">
  <path d="M0 44 L526 5 L755 44 L755 274 L0 274 Z" fill="var(--charcoal)"/>
  <path d="M0 44 L526 5 L755 44" fill="none" stroke="var(--gold)" stroke-width="3"/>
</svg>
<div class="abs f-brand"><span>HC</span><span class="brand-dot"></span></div>
<p class="abs f-text" style="left:123px;top:1045px">Ashgrove Lane Ballyrowan Co.</p>
<p class="abs f-text" style="left:123px;top:1063px">Kildare Ireland</p>
<svg class="abs" style="left:124px;top:1080px" width="12" height="12" viewBox="0 0 12 12"><path d="M2 1 l2 0 l1 3 l-1.5 1 a7 7 0 0 0 3.5 3.5 l1-1.5 l3 1 l0 2 a1 1 0 0 1-1 1 A10 10 0 0 1 1 2 a1 1 0 0 1 1-1z" fill="#fff"/></svg>
<p class="abs f-text" style="left:146px;top:1085px">+353 87 204 3917</p>
<svg class="abs" style="left:124px;top:1102px" width="13" height="10" viewBox="0 0 13 10"><rect x=".5" y=".5" width="12" height="9" fill="none" stroke="#fff"/><path d="M.5 .5 l6 5 l6-5 M.5 9.5 l4.5-4 M12.5 9.5 l-4.5-4" fill="none" stroke="#fff"/></svg>
<p class="abs f-text" style="left:146px;top:1105px">helena@helenacarrowmere.com</p>
<div class="abs social" style="left:125px"></div>
<div class="abs social" style="left:140px"></div>
<div class="abs social" style="left:155px"></div>
<div class="abs social" style="left:170px"></div>

<h2 class="abs links-title">Useful Links</h2>
<nav class="links">
  <a style="top:1020px">Home</a>
  <a style="top:1039px">About</a>
  <a style="top:1058px">Horses</a>
  <a style="top:1076px">Sponsors</a>
  <a style="top:1095px">Facilities &amp; Services</a>
  <a style="top:1114px">Gallery</a>
  <a style="top:1133px">Contact Us</a>
</nav>
<div class="abs map" role="img" aria-label="Map showing the yard location in County Kildare"></div>

<footer class="abs copyright">Copyright ©2020 HC. All Rights Reserve</footer>
</body>
</html>
```